Lumora aesthetics offers a range of facial aesthetics treatments by a fully qualified dentist, to a high end crowd. Treatments include antiwrinkle treatment, the use of dermal fillers to provide facial volumisation and rejuvenation and also lip volumisation.
I want a luxurious and bold look. Black background with a bold striking gold logo in the centre possibly incorporating the outline of a face in a subtle yet effective way. I want it to include the work I offer so people will be aware of what they are looking into but not look like there's too much on the card, So it's a clean look.
At the bottom I would like it to say by Dr. Meera Sandhu. Alongside my email address and mobile number.

```html
<!DOCTYPE html>
<html lang="en">
<head>
<meta charset="UTF-8">
<title>Lumora Aesthetics – Business Card</title>
<link rel="stylesheet" href="https://fonts.googleapis.com/css2?family=Exo+2:wght@700&family=Open+Sans:wght@400;600&display=swap">
<style>
  :root {
    --page-bg: #ecebe8;
    --card-black: #232124;
    --card-edge: #2c292d;
    --gold: #b8925a;
    --gold-light: #c9a46a;
    --text-white: #f2f0ec;
    --text-grey: #a9a6a8;
    --shadow: rgba(0, 0, 0, 0.28);
  }
  * { box-sizing: border-box; margin: 0; padding: 0; }
  html, body {
    width: 1200px;
    height: 1000px;
    overflow: hidden;
    background: var(--page-bg);
  }
  .canvas {
    position: relative;
    width: 1200px;
    height: 1000px;
  }
  .business-card {
    position: absolute;
    left: 150px;
    top: 240px;
    width: 900px;
    height: 520px;
    background: linear-gradient(135deg, var(--card-edge) 0%, var(--card-black) 60%);
    border-radius: 6px;
    box-shadow: 0 20px 50px var(--shadow);
    overflow: hidden;
    font-family: "Open Sans", Arial, sans-serif;
  }
  .brand-name {
    position: absolute;
    left: 60px;
    top: 58px;
    font-family: "Exo 2", "Arial Black", sans-serif;
    font-weight: 700;
    font-size: 62px;
    letter-spacing: 2px;
    color: var(--gold);
    text-transform: uppercase;
    white-space: nowrap;
  }
  .practitioner-name {
    position: absolute;
    left: 60px;
    top: 148px;
    font-family: "Exo 2", "Arial Black", sans-serif;
    font-weight: 700;
    font-size: 38px;
    letter-spacing: 1.5px;
    color: var(--gold-light);
    text-transform: uppercase;
  }
  .treatment-list {
    position: absolute;
    left: 66px;
    top: 212px;
    list-style: none;
    color: var(--text-white);
    font-size: 21px;
    line-height: 27px;
  }
  .address {
    position: absolute;
    left: 66px;
    top: 318px;
    color: var(--text-grey);
    font-size: 22px;
    line-height: 29px;
  }
  .contact-list {
    position: absolute;
    left: 66px;
    top: 398px;
    list-style: none;
    color: var(--text-white);
    font-size: 23px;
    line-height: 32px;
  }
  .contact-label { color: var(--gold); }
  .profile-decoration {
    position: absolute;
    right: 40px;
    bottom: 30px;
    width: 360px;
    height: 290px;
    background: radial-gradient(ellipse at 60% 50%, rgba(255,255,255,0.05) 0%, rgba(255,255,255,0) 70%);
  }
</style>
</head>
<body>
<main class="canvas">
  <section class="business-card">
    <h1 class="brand-name">Lumora Aesthetics</h1>
    <h2 class="practitioner-name">Dr. Meera Sandhu</h2>
    <ul class="treatment-list">
      <li>Antiwrinkle Treatment</li>
      <li>Facial Volumisation</li>
      <li>Lip Volumisation</li>
    </ul>
    <p class="address">Your Street Address,<br>Singapore, 1234</p>
    <ul class="contact-list">
      <li><span class="contact-label">Email:</span> yourname@email.com</li>
      <li><span class="contact-label">Phone:</span> +000 123 456 789</li>
    </ul>
    <div class="profile-decoration" role="img" aria-label="Faint line illustration of a woman's profile with flowing hair"></div>
  </section>
</main>
</body>
</html>
```